Contemporary Business card for Event Manager

Needed for my startup events company in Melbourne. Events I manage will be based within the fashion industry, sporting events, product launches etc. Not weddings or small dinner parties. Therfore I am after something professional and aimed at high end corporate market; but with the added emphasis on not being too conservative or boring. I am happy with a pop of colour e.g. yellow or copper foil.

Target Market(s)

fashion industry, design industry, high end sporting events e.g. Polo, Grand Prix, corporate clients,

Industry/Entity Type

Fashion

Contact Information for Business Card

side 1
Rosa Whitfield (can be upper or lower case, have a feature full stop between first and surname, or at the end of the nameetc) I am open to ideas. I would also be fine with my initials or name as a logo on the front (if this is the case my full name would need to go on the second side of the card.
2nd side:
Mobile: +61 455 718 263
email: rosa.whitfield@kestrelpost.com.au

on one side of the card:
event management | brand activation | Advisory Services

Font styles to use
Serif
Sans Serif

Requirements
Must have
• side 2 must have
• mobile number
• email address
• event management | brand activation | Advisory Services
• ** my full name (Rosa Whitfield) must be on the card somewhere)
Nice to have
• 1st side
• I see the card stock being either a dark grey, light grey, natural white or black (all matt colours on unprocessed card). I see the writing being copper foil, or foil white or foil black.
• To give you a feel for me, think: contemporary, minimalist, I love line drawings, concrete, white with grey vein marble, copper, white, grey, black...yes I do like colour....yellow (but pops of colour) ;) I would like the card to look designer but 'on trend' as I deal with a lot of design and fashion clients....styles - think the sophistication and simplicity of Lisoret or urban contemporary.
• some examples of what I like. Although please don't leet this limit you...I really am happy to have something a little more urban or design focused like a line drawing of an object, person too or a photo image too.
• https://www.pinvaultly.com/pin/837205164932850174/
• https://www.pinvaultly.com/pin/926318450173648205/
• https://www.pinvaultly.com/pin/318604927551203847/
• https://www.pinvaultly.com/pin/50938162477420916/
• https://www.pinvaultly.com/pin/41276039158862793/
• https://www.pinvaultly.com/pin/63098817524506139/
• https://www.pinvaultly.com/pin/704129583366208154/
• https://www.pinvaultly.com/pin/582046317729851460/
• https://www.pinvaultly.com/pin/467318205542097831/
Should not have
• should not look commercial or have cartoonish looking logos. However happy with a simple line drawing or logo with initials etc.

```html
<!DOCTYPE html>
<html lang="en">
<head>
<meta charset="utf-8">
<title>Rosa Whitfield — Business Card</title>
<link rel="stylesheet" href="https://fonts.googleapis.com/css2?family=Crimson+Pro:wght@700&display=swap">
<style>
  :root {
    --backdrop: #d9d9d9;
    --card-stock: #1b1b1b;
    --foil-yellow: #ffe500;
    --card-w: 856px;
    --card-h: 488px;
  }
  * { margin: 0; padding: 0; box-sizing: border-box; }
  html, body {
    width: 1189px;
    height: 1200px;
    overflow: hidden;
    background: var(--backdrop);
  }
  .sheet {
    position: relative;
    width: 1189px;
    height: 1200px;
  }
  .card {
    position: absolute;
    left: 171px;
    width: var(--card-w);
    height: var(--card-h);
    background: var(--card-stock);
    border-radius: 20px;
    color: var(--foil-yellow);
    font-family: "Crimson Pro", Georgia, serif;
    font-weight: 700;
    text-align: center;
  }
  .card--front { top: 67px; }
  .card--back  { top: 627px; }
  .line {
    position: absolute;
    left: 0;
    right: 0;
    white-space: nowrap;
  }
  .name {
    font-size: 98px;
    line-height: 110px;
    letter-spacing: 1px;
  }
  .card--front .name { top: 189px; }
  .card--back .name  { top: 69px; }
  .phone {
    top: 200px;
    font-size: 68px;
    line-height: 76px;
    letter-spacing: 1px;
  }
  .email {
    top: 276px;
    font-size: 36px;
    line-height: 40px;
    letter-spacing: 1px;
  }
  .services {
    top: 366px;
    font-size: 29px;
    line-height: 34px;
    letter-spacing: 0.5px;
  }
  .services .divider { margin: 0 6px; }
</style>
</head>
<body>
  <main class="sheet">
    <section class="card card--front" aria-label="Card front">
      <h1 class="line name">Rosa Whitfield</h1>
    </section>
    <section class="card card--back" aria-label="Card back">
      <p class="line name">Rosa Whitfield</p>
      <p class="line phone">+61 455 718 263</p>
      <p class="line email">rosa.whitfield@kestrelpost.com.au</p>
      <p class="line services">event management<span class="divider">|</span>brand activation<span class="divider">|</span>Advisory Services</p>
    </section>
  </main>
</body>
</html>
```